Corvanta Business cards template

We're looking for something modern and elegant. We are a reseller of technology (computers, datacenter, etc). Color theme would be "only" white with the incorporation of the blue that's present on our website (Corvanta.com) and logo file. We would like for the card to provide all the necessary info for the specific person (Phone#, fax#, email, name, website URL) . I'm attaching the logo file to this request. Please have it show Montreal/New York somewhere, without providing specific addresses.

Target Market(s)

All b2b

Industry/Entity Type

Business

Contact Information for Business Card

Please have the color scheme be represented by only the white and blue from our website (Corvanta.com) and logo. We would like to logo on the card, but not big and overwhelming. This card will be used as a template for anybody within the company, it should display the user's name, phone#, fax#, email, job title and website URL. Please have it show Montreal/New York somewhere, without providing our specific addresses. Really, we're looking for a clean, simple and elegant look.

Font styles to use
Serif

Requirements
Must have
• Please see card details
Nice to have
• Please see card details
Should not have
• Anything tacky or tagline.

```html
<!DOCTYPE html>
<html lang="en">
<head>
<meta charset="utf-8">
<title>Corvanta Business Card</title>
<link rel="stylesheet" href="https://fonts.googleapis.com/css2?family=Lora:wght@400;500;700&display=swap">
<style>
  :root {
    --backdrop: #c9c9c9;
    --card-white: #ffffff;
    --brand-blue: #0a6fc2;
    --ink: #2b2b2b;
  }
  * { box-sizing: border-box; margin: 0; padding: 0; }
  html, body {
    width: 1200px;
    height: 1000px;
    overflow: hidden;
    background: var(--backdrop);
    font-family: "Lora", serif;
  }
  .stage {
    position: relative;
    width: 1200px;
    height: 1000px;
  }
  .card {
    position: absolute;
    top: 340px;
    width: 540px;
    height: 320px;
    background: var(--card-white);
    box-shadow: 0 4px 14px rgba(0,0,0,0.18);
  }
  .card-front { left: 40px; }
  .card-back { left: 620px; }

  .wordmark {
    position: absolute;
    color: var(--brand-blue);
    font-weight: 400;
    letter-spacing: 0.5px;
    line-height: 1;
  }
  .card-front .wordmark { left: 40px; top: 128px; font-size: 34px; }
  .card-back .wordmark {
    left: 0; right: 0; top: 140px;
    text-align: center;
    font-size: 40px;
  }

  .divider {
    position: absolute;
    left: 300px;
    width: 2px;
    background: var(--brand-blue);
  }
  .divider-name { top: 96px; height: 40px; }
  .divider-contact { top: 146px; height: 88px; }

  .person {
    position: absolute;
    left: 318px;
    top: 96px;
  }
  .person-name {
    color: var(--brand-blue);
    font-weight: 700;
    font-size: 19px;
    letter-spacing: 0.6px;
    text-transform: uppercase;
    line-height: 1.1;
  }
  .person-title {
    color: var(--ink);
    font-weight: 700;
    font-size: 11px;
    letter-spacing: 0.6px;
    text-transform: uppercase;
    margin-top: 3px;
  }

  .contact-list {
    position: absolute;
    left: 318px;
    top: 148px;
    list-style: none;
  }
  .contact-item {
    display: flex;
    align-items: center;
    gap: 10px;
    height: 21px;
    font-size: 14px;
    color: var(--ink);
    letter-spacing: 0.3px;
  }
  .contact-item svg { width: 12px; height: 12px; fill: var(--brand-blue); flex: none; }
  .contact-web { color: var(--brand-blue); font-weight: 500; }

  .locations {
    position: absolute;
    left: 0; right: 0;
    bottom: 30px;
    text-align: center;
    font-size: 13px;
    color: var(--ink);
    letter-spacing: 0.4px;
  }
</style>
</head>
<body>
<main class="stage">

  <section class="card card-front" aria-label="Business card front">
    <div class="wordmark">Corvanta</div>

    <span class="divider divider-name"></span>
    <span class="divider divider-contact"></span>

    <div class="person">
      <div class="person-name">Daniel Reyes</div>
      <div class="person-title">Founder</div>
    </div>

    <ul class="contact-list">
      <li class="contact-item">
        <svg viewBox="0 0 12 12" aria-hidden="true"><path d="M2.5 1 L4.5 1 L5.3 3.6 L4 4.6 Q5 7 7.4 8 L8.4 6.7 L11 7.5 L11 9.5 Q11 11 9.5 11 Q1 10.5 1 2.5 Q1 1 2.5 1 Z"/></svg>
        <span>000 000 0000</span>
      </li>
      <li class="contact-item">
        <svg viewBox="0 0 12 12" aria-hidden="true"><rect x="3" y="1" width="6" height="3"/><rect x="1" y="4.5" width="10" height="5" rx="1"/><rect x="3" y="8" width="6" height="3"/></svg>
        <span>000 000 0000</span>
      </li>
      <li class="contact-item">
        <svg viewBox="0 0 12 12" aria-hidden="true"><path d="M1 2.5 H11 V9.5 H1 Z M1.6 3 L6 6.4 L10.4 3 Z" fill-rule="evenodd"/></svg>
        <span>info@danielreyes.com</span>
      </li>
      <li class="contact-item">
        <svg viewBox="0 0 12 12" aria-hidden="true"><path d="M7 1 A4 4 0 1 1 7 9 A4 4 0 1 1 7 1 Z M7 2.5 A2.5 2.5 0 1 0 7 7.5 A2.5 2.5 0 1 0 7 2.5 Z" fill-rule="evenodd"/><rect x="0.5" y="8.6" width="4.2" height="1.6" transform="rotate(-45 2.6 9.4)"/></svg>
        <span class="contact-web">Corvanta.com</span>
      </li>
    </ul>

    <p class="locations">Montreal / New York</p>
  </section>

  <section class="card card-back" aria-label="Business card back">
    <div class="wordmark">Corvanta</div>
  </section>

</main>
</body>
</html>
```